Gardening and life coaching business card design

I need business cards for a new company in the heart of the Ozarks at the Lake of the Ozarks. Tallow Brook Harvest's mission is to teach the world to fish. We provide fresh local fish and produce using permaculture methods. We work with nature and the flow to create more harmony and less impact. We also coach others who are ready to make this transition. We specialize in microgreens and Aquaculture systems. I would like to make Tallow Brook Harvest come alive with green vines and purple flowers I wold like Tallow Brook Harvest to be in green and the rest of the lettering to be in purple. The feel of the card should be that of the Garden of Eden.

Industry/Entity Type

Life Coaching

Contact Information for Business Card

Tallow Brook Harvest
Owner/Operator Marisol Pettigrew
Contact Info:
(555) 214-9083
tallowbrookharvest.example
tallowbrookharvest is also on FB

```html
<!DOCTYPE html>
<html lang="en">
<head>
<meta charset="utf-8">
<title>Tallow Brook Harvest — Business Card</title>
<link rel="stylesheet" href="https://fonts.googleapis.com/css2?family=Stardos+Stencil:wght@700&family=Tinos&display=swap">
<style>
  :root {
    --bg: #e9e4dc;
    --paper: #ffffff;
    --ink: #111111;
    --leaf: #2f5a26;
    --leaf-deep: #1f4219;
    --leaf-light: #43732f;
    --rule: #0d0d0d;
    --on-green: #f4f4ee;
  }
  * { box-sizing: border-box; margin: 0; padding: 0; }
  html, body { width: 1200px; height: 848px; overflow: hidden; }
  body {
    background: var(--bg);
    display: flex;
    flex-direction: column;
    align-items: center;
    justify-content: center;
    gap: 40px;
    font-family: "Tinos", "Times New Roman", serif;
  }
  .card {
    position: relative;
    width: 640px;
    height: 366px;
    border-radius: 26px;
    overflow: hidden;
    background: var(--paper);
    box-shadow: 0 6px 18px rgba(0,0,0,0.18);
  }
  .card__band { position: absolute; inset: 0; width: 100%; height: 100%; }
  .card__text { position: absolute; }

  .person__name { font-size: 33px; color: var(--ink); line-height: 1; white-space: nowrap; }
  .person__title { font-size: 17px; color: var(--ink); text-align: right; margin-top: 2px; line-height: 1.1; }

  .brand {
    font-family: "Stardos Stencil", "Impact", sans-serif;
    font-weight: 700;
    text-transform: uppercase;
    line-height: 0.95;
    letter-spacing: 0.5px;
  }

  /* front */
  .front .person { left: 78px; top: 96px; }
  .front .brand { right: 48px; top: 44px; font-size: 36px; color: var(--ink); text-align: center; }
  .front .contact {
    left: 0; right: 0; top: 232px;
    text-align: center;
    color: var(--on-green);
    font-size: 22px;
    line-height: 1.3;
  }

  /* back: divider runs from (0,212) to (640,58), about 13.5deg */
  .back .person {
    left: 300px; top: 86px;
    height: 42px;
    transform: rotate(-13.5deg);
    transform-origin: left bottom;
  }
  .back .person__name { font-size: 24px; }
  .back .person__title { font-size: 13px; }
  .back .brand {
    left: 112px; top: 238px;
    font-size: 40px;
    color: var(--on-green);
    white-space: nowrap;
    transform: rotate(-13.5deg);
    transform-origin: left top;
  }
</style>
</head>
<body>

<section class="card front">
  <svg class="card__band" viewBox="0 0 640 366" preserveAspectRatio="none" role="img" aria-label="Dim green forest photograph of tall trees and leaves">
    <defs>
      <linearGradient id="forestFront" x1="0" y1="0" x2="1" y2="1">
        <stop offset="0" stop-color="#43732f"/>
        <stop offset="0.5" stop-color="#2f5a26"/>
        <stop offset="1" stop-color="#1f4219"/>
      </linearGradient>
    </defs>
    <polygon points="0,178 640,150 640,366 0,366" fill="url(#forestFront)"/>
    <line x1="0" y1="178" x2="640" y2="150" stroke="#0d0d0d" stroke-width="3"/>
  </svg>
  <div class="card__text person">
    <p class="person__name">Marisol Pettigrew</p>
    <p class="person__title">Owner/Operator</p>
  </div>
  <p class="card__text brand">Tallow Brook<br>Harvest</p>
  <div class="card__text contact">
    <p>P: (555) 214-9083</p>
    <p>w: tallowbrookharvest.example</p>
    <p>f: tallowbrookharvest</p>
  </div>
</section>

<section class="card back">
  <svg class="card__band" viewBox="0 0 640 366" preserveAspectRatio="none" role="img" aria-label="Dim green forest photograph of tall trees and leaves">
    <defs>
      <linearGradient id="forestBack" x1="0" y1="0" x2="1" y2="1">
        <stop offset="0" stop-color="#43732f"/>
        <stop offset="0.5" stop-color="#2f5a26"/>
        <stop offset="1" stop-color="#1f4219"/>
      </linearGradient>
    </defs>
    <polygon points="0,212 640,58 640,366 0,366" fill="url(#forestBack)"/>
    <line x1="0" y1="212" x2="640" y2="58" stroke="#0d0d0d" stroke-width="3"/>
  </svg>
  <div class="card__text person">
    <p class="person__name">Marisol Pettigrew</p>
    <p class="person__title">Owner/Operator</p>
  </div>
  <p class="card__text brand">Tallow Brook Harvest</p>
</section>

</body>
</html>
```